Business card design for a dynamic IT consulting company

We need a business card design for a young firm, specialized in the Telecommunications/Consulting industry. The name of the company is Brask and Partners Business Consulting Ltd. (Short name: Brask and Partnes)
Brask = solve read reverse, so we aim to be uncomplicated and solution-oriented. The small pipe in our logo is also related to the word solve. So we need a new business card design, which is simple, eye catching and something non traditional (I would probably prefer a square shaped design rather than a rectangle, but open for suggestions). Attached our logo.

Target Market(s)

Usually our customers are Tier1 Telecoms providers (Q-Linkra, Parnexo, etc) and their executives.

Industry/Entity Type

Business

Contact Information for Business Card

Name: Gergely Halmindo
Email: g.halmindo@braskpartnera.hu
Web: www.braskpartnera.hu
Mobile: +36 30 555 0192
Title: Managing Director

Optional:
Company name: Brask and Partners Ltd.
Address: 1047 Budapest, Ravaszi str. 17/B, Hungary

Font styles to use
Other font styles liked:
• helveticaneue_medium, Prime Regular are used now.

Colors

Designer to choose colors to be used in the design.

Requirements
Must have
• I would like to have a 2 sided design.
Nice to have
• I thought if we make the logo a bit bigger (without the company name), that could go to the back with the company name below. I though, if the pipe in the logo is somehow touchable on the business card, would be nice and unique.

```html
<!DOCTYPE html>
<html lang="en">
<head>
<meta charset="utf-8">
<title>Brask and Partners – Business Card</title>
<link rel="stylesheet" href="https://fonts.googleapis.com/css2?family=Inter:wght@300;400;700&display=swap">
<style>
  :root {
    --stage: #999999;
    --paper: #ffffff;
    --ink: #000000;
    --logo-grey: #6b6b6b;
    --magenta: #b72e8e;
    --cyan: #0096d6;
    --text-dark: #1a1a1a;
  }
  * { margin: 0; padding: 0; box-sizing: border-box; }
  html, body {
    width: 1200px; height: 1200px; overflow: hidden;
    background: var(--stage);
    font-family: "Inter", "Helvetica Neue", Arial, sans-serif;
  }
  .card {
    position: absolute;
    left: 135px;
    width: 930px;
    height: 531px;
    overflow: hidden;
  }
  .card--front { top: 44px; background: var(--paper); }
  .card--back { top: 600px; background: var(--ink); }

  .brand {
    position: absolute;
    left: 63px; top: 62px;
    display: flex; align-items: center; gap: 18px;
  }
  .brand__square { width: 30px; height: 30px; background: var(--magenta); }
  .brand__name {
    font-weight: 400; font-size: 56px; line-height: 1;
    color: var(--logo-grey); letter-spacing: -0.5px;
  }

  .person {
    position: absolute; left: 45px; top: 298px;
    font-size: 52px; line-height: 1; letter-spacing: -1.5px;
    color: var(--ink); white-space: nowrap;
  }
  .person__first { font-weight: 700; }
  .person__last { font-weight: 300; }

  .rule {
    position: absolute; left: 0; right: 0; top: 378px; height: 8px;
    background: var(--ink);
  }
  .role {
    position: absolute; left: 39px; top: 369px;
    width: 335px; height: 37px;
    background: var(--ink);
    clip-path: polygon(0 0, 100% 0, 97% 100%, 3% 100%);
    color: var(--paper); font-weight: 700; font-size: 23px;
    line-height: 37px; padding-left: 35px; letter-spacing: 0.2px;
  }
  .company {
    position: absolute; left: 45px; top: 409px;
    font-weight: 700; font-size: 33px; color: var(--text-dark);
    letter-spacing: 0.2px;
  }
  .address {
    position: absolute; left: 45px; top: 458px;
    font-weight: 400; font-size: 18.5px; line-height: 24px;
    color: var(--text-dark);
  }

  .contact {
    position: absolute; right: 0;
    height: 37px; background: var(--ink);
    color: var(--paper); font-weight: 700; font-size: 22px;
    line-height: 37px; text-align: right; padding-right: 25px;
    clip-path: polygon(0 0, 100% 0, 100% 100%, 40px 100%);
    white-space: nowrap;
  }
  .contact--phone { top: 397px; width: 245px; }
  .contact--email { top: 441px; width: 405px; }
  .contact--web { top: 485px; width: 300px; }

  .back-brand {
    position: absolute; inset: 0;
    display: flex; align-items: center; justify-content: center; gap: 20px;
  }
  .back-brand__square { width: 34px; height: 34px; background: var(--cyan); }
  .back-brand__name {
    font-weight: 400; font-size: 54px; color: var(--paper);
    letter-spacing: -0.5px;
  }
</style>
</head>
<body>
  <section class="card card--front">
    <div class="brand">
      <span class="brand__square"></span>
      <span class="brand__name">Brask &amp; Partners</span>
    </div>

    <h1 class="person"><span class="person__first">GERGELY</span> <span class="person__last">HALMINDO</span></h1>

    <div class="rule"></div>
    <div class="role">MANAGING DIRECTOR</div>

    <p class="company">Brask and Partners Ltd.</p>
    <p class="address">1047 Budapest, Ravaszi str.<br>17/B, Hungary</p>

    <div class="contact contact--phone">+36 30 555 0192</div>
    <div class="contact contact--email">g.halmindo@braskpartnera.hu</div>
    <div class="contact contact--web">www.braskpartnera.hu</div>
  </section>

  <section class="card card--back">
    <div class="back-brand">
      <span class="back-brand__square"></span>
      <span class="back-brand__name">Brask &amp; Partners</span>
    </div>
  </section>
</body>
</html>
```